DM - management consultant

Business card - contemporary design

Front info
Dorian Maples

(Address not necessary)
PO Box 7386
Belmont, CA 94002

(650) 555-0143
dm@dorianmapl.es

Murmur: dmq527
Hearthly: /Dorian.Maples
Workgrid: /in/dorianmaples

Back or Front
www.dorianmaples.net
Facilitation & coaching, change management, strategic partnerships, business improvement

Target Market(s)

High tech businesses - mostly startups in Silicon Valley

Industry/Entity Type

Business

Font styles to use
Sans Serif

Colors

Designer to choose colors to be used in the design.

```html
<!DOCTYPE html>
<html lang="en">
<head>
<meta charset="utf-8">
<title>Dorian Maples – Business Card</title>
<link rel="stylesheet" href="https://fonts.googleapis.com/css2?family=Inter:wght@300;400&display=swap">
<style>
  :root {
    --page: #ffffff;
    --card: #1f818c;
    --ink: #ffffff;
    --rule-front: rgba(255, 255, 255, 0.75);
    --rule-back: #8fd0d6;
    --shadow: rgba(0, 0, 0, 0.55);
  }
  * { margin: 0; padding: 0; box-sizing: border-box; }
  html, body {
    width: 846px;
    height: 1200px;
    overflow: hidden;
    background: var(--page);
  }
  body {
    position: relative;
    font-family: "Inter", "Helvetica Neue", Arial, sans-serif;
    font-weight: 300;
    color: var(--ink);
  }
  .card {
    position: absolute;
    background: var(--card);
    box-shadow: 5px 6px 8px var(--shadow);
  }
  .card--front { left: 86px; top: 198px; width: 655px; height: 385px; }
  .card--back  { left: 86px; top: 646px; width: 666px; height: 390px; }

  .card__name {
    position: absolute;
    left: 93px;
    top: 84px;
    font-size: 20px;
    font-weight: 400;
    letter-spacing: 0.5em;
    line-height: 1;
    text-transform: uppercase;
    white-space: nowrap;
  }
  .card__contact,
  .card__social {
    position: absolute;
    list-style: none;
    font-size: 17px;
    line-height: 25.6px;
    white-space: nowrap;
  }
  .card__contact { left: 93px; top: 120px; }
  .card__social  { left: 337px; top: 238px; }

  .card__rule {
    position: absolute;
    height: 1px;
  }
  .card--front .card__rule { left: 93px; top: 216px; width: 358px; background: var(--rule-front); }
  .card--back .card__rule  { left: 114px; top: 230px; width: 407px; background: var(--rule-back); }

  .card__services {
    position: absolute;
    left: 117px;
    top: 165px;
    font-size: 18.5px;
    line-height: 24.5px;
    white-space: nowrap;
  }
</style>
</head>
<body>
  <section class="card card--front" aria-label="Card front">
    <h1 class="card__name">Dorian Maples</h1>
    <ul class="card__contact">
      <li>(650) 555-0143</li>
      <li>dm@dorianmapl.es</li>
      <li>www.dorianmaples.net</li>
    </ul>
    <div class="card__rule"></div>
    <ul class="card__social">
      <li>Murmur: dmq527</li>
      <li>Hearthly: /Dorian.Maples</li>
      <li>Workgrid: /in/dorianmaples</li>
    </ul>
  </section>

  <section class="card card--back" aria-label="Card back">
    <p class="card__services">Facilitation &amp; coaching, change management,<br>strategic partnerships, business improvement.</p>
    <div class="card__rule"></div>
  </section>
</body>
</html>
```